Concept design for a tea business Labels

Hello, we are looking for concepts for our label/packaging for a tea business that has been in business now for over a year. We are a beachy, organic, "Slow down. Savour every sip." type tea business. We have an online website (www.corvalbrewhouse.com.au) and sell at local markets around the Tarrowby Cove area.
We are looking to upgrade our label to look more professional, in a fun/beachy/chilled out style. (unlike the traditional tea labels).
We do loose leaf tea and iced tea consentrated syrups. We have a few different packages (please see website under "sizes and packaging" bottom left). We would like to experiement with various different size and shape of labels for different products, so would like a concept design for a label using our logo (see website front page bottom). There are no colour constraints.
We use the Quillan brand labels of the following sizes:
1. Pure Glass Rectangular Product Labels, Q4825, 100/Pack, 96 x 50.8 mm
2. Pure Glass Round Multi-purpose Labels, Q3907D, 240/Pack, 40 mm diameter
3.Pure Glass Square Product Labels, Q4861, 350/Pack, 35 x 35 mm
4. For bottles we use Grained Ivory Curved Labels, Q4839, 90/Pack, 57.2 x 77 mm
If you have any more questions, please don't hesitate to contact me
Updates
Hi All,
I am considering using a box like below for packing and doing a bit of a white/beachy feel to the packaging. Either using the rectangle or round circle labels. (circle labels from quillan 60mm diameter).

Reason: Hi All - Thank you so much for all your designs. While I have seen some really beautiful designs I am excited about, it seems there was a rush at the end with a number of new designs just submitted. I still haven't seen just one design I love for the label, so I would like the opportunity to work with some of the new designers to see if we can modify to suit the concept.
Would anyone like to try a concept label with a silhouette of one of the following wave/beach/teacup? I'm just exploring a different approach as I know it is difficult tying in the beach with tea - please think - chilled out beach hut with tea/iced tea, sunrise over ocean. I like the soft colour palette - beachy feel to it - ie. Pastels - blues, greens, whites, sandy, pinks, purples, greys - sunrises over ocean, maybe a white rustic wood feel - or any other icon from Tarrowby Cove - like the Norfolk Pine's along the beach - maybe in Silhouette.
Just some more ideas.
Thank you again for all your contributions!
Petra

```html
<!DOCTYPE html>
<html lang="en">
<head>
<meta charset="UTF-8">
<title>Tarrowby Tea Company – Round Label Concept</title>
<link rel="stylesheet" href="https://fonts.googleapis.com/css2?family=Crimson+Text:ital,wght@0,400;0,700;1,400&display=swap">
<style>
  :root {
    --backdrop-light: #cdc7c6;
    --backdrop-dark: #aba4a3;
    --sky-deep: #1fb3ec;
    --sky-soft: #6ccbf1;
    --cloud-white: #ffffff;
    --sea-blue: #22b2ea;
    --sea-pale: #a5dcf5;
    --foam: #eef8fd;
    --sand: #f7e0b5;
    --sun-orange: #ef7a3e;
    --ink: #333333;
    --dash: #8fd3f4;
  }

  * { margin: 0; padding: 0; box-sizing: border-box; }

  html, body {
    width: 1200px;
    height: 553px;
    overflow: hidden;
  }

  body {
    background: radial-gradient(ellipse at 70% 30%, var(--backdrop-light), var(--backdrop-dark));
    position: relative;
  }

  .round-label {
    position: absolute;
    left: 360px;
    top: 36px;
    width: 480px;
    height: 480px;
    border-radius: 50%;
    overflow: hidden;
    box-shadow: 0 4px 18px rgba(0, 0, 0, 0.12);
  }

  .round-label__scene {
    position: absolute;
    inset: 0;
    width: 100%;
    height: 100%;
  }

  .brand__mark {
    position: absolute;
    left: 180px;
    top: 84px;
    width: 120px;
    height: 120px;
    border-radius: 50%;
    background: var(--sun-orange);
  }

  .brand__name {
    position: absolute;
    left: 0;
    right: 0;
    top: 210px;
    text-align: center;
    color: var(--ink);
    font-family: "Crimson Text", Georgia, serif;
    text-transform: uppercase;
    line-height: 1;
  }

  .brand__name-line {
    display: block;
    font-weight: 700;
    font-size: 42px;
    letter-spacing: 0.5px;
  }

  .brand__name-line--small {
    font-weight: 400;
    font-size: 30px;
    letter-spacing: 1px;
    margin-top: 2px;
  }

  .tagline {
    position: absolute;
    left: 0;
    right: 0;
    top: 350px;
    text-align: center;
    font-family: "Crimson Text", Georgia, serif;
    font-style: italic;
    font-weight: 400;
    font-size: 22px;
    color: var(--ink);
  }
</style>
</head>
<body>
  <div class="round-label">
    <svg class="round-label__scene" viewBox="0 0 480 480" role="img" aria-label="Soft beach scene: blue sky with bubbles, white clouds on the horizon, calm blue sea and a strip of sand">
      <defs>
        <linearGradient id="beach-gradient" x1="0" y1="0" x2="0" y2="1">
          <stop offset="0" stop-color="var(--sky-deep)"/>
          <stop offset="0.46" stop-color="var(--sky-soft)"/>
          <stop offset="0.53" stop-color="var(--foam)"/>
          <stop offset="0.635" stop-color="var(--cloud-white)"/>
          <stop offset="0.635" stop-color="var(--sea-blue)"/>
          <stop offset="0.8" stop-color="var(--sea-pale)"/>
          <stop offset="0.885" stop-color="var(--foam)"/>
          <stop offset="0.9" stop-color="var(--sand)"/>
          <stop offset="1" stop-color="var(--sand)"/>
        </linearGradient>
      </defs>
      <rect class="scene__fill" width="480" height="480" fill="url(#beach-gradient)"/>
      <circle class="scene__dashed-ring" cx="240" cy="240" r="224" fill="none" stroke="var(--dash)" stroke-width="1.5" stroke-dasharray="4 4"/>
    </svg>

    <span class="brand__mark"></span>
    <h1 class="brand__name">
      <span class="brand__name-line">Tarrowby Tea</span>
      <span class="brand__name-line brand__name-line--small">Company</span>
    </h1>

    <p class="tagline">Slow down. Savour every sip.</p>
  </div>
</body>
</html>
```